tri-fold brochure design for psychology practice - all content provided

we are a psychology practice that specialises in diagnostic and educational assessments for children, adolescents and adults. We have an existing logo and I am attaching a word doc (tri-fold brochure) with the required content. I am also attaching our logo and other relevant content docs. The layout is only a sample and we are looking for someone to put this together into a consistent and better layout.

Target Market(s)

parents

Industry/Entity Type

education and health

Font styles to use
Other font styles liked:
• crimsonpro

Requirements
Must have
• our logo and the provided content

```html
<!DOCTYPE html>
<html lang="en">
<head>
<meta charset="utf-8">
<title>rootwell – tri-fold brochure</title>
<link rel="stylesheet" href="https://fonts.googleapis.com/css2?family=Crimson+Pro:wght@400;600;700&family=Work+Sans:wght@400;500;600&display=swap">
<style>
:root{
  --green:#679b3a;
  --green-dark:#4f8426;
  --leaf:#8db653;
  --leaf-pale:#dbe9c6;
  --yellow:#fddb5a;
  --blue:#5b9bd5;
  --teal:#4cc48c;
  --ink:#333333;
  --ink-soft:#4a4a4a;
  --paper:#ffffff;
  --canvas:#e9e9e9;
  --label:#9a9a9a;
  --bark:#5a3d2b;
  --head:"Crimson Pro", Georgia, serif;
  --body:"Work Sans", Arial, sans-serif;
}
*{box-sizing:border-box;margin:0;padding:0}
html,body{width:1200px;height:2748px;overflow:hidden;background:var(--canvas)}
.canvas{position:relative;width:1200px;height:2748px;overflow:hidden;background:var(--canvas);font-family:var(--body);color:var(--ink)}
.abs{position:absolute}
.spread-label{position:absolute;font-family:var(--body);font-weight:500;font-size:25px;letter-spacing:.5px;color:var(--label)}
.spread{position:absolute;background:var(--paper);box-shadow:0 2px 6px rgba(0,0,0,.15);overflow:hidden}
.panel{position:absolute;top:0;bottom:0}
.branch{position:absolute;background:linear-gradient(160deg,#f4f1ec 0%,#e9e1d6 45%,#e4eed5 100%)}
.leaf-pattern{position:absolute;background:linear-gradient(180deg,#eef5e4 0%,#f7faf2 100%)}
.brand{font-family:var(--head);font-weight:600;color:var(--green);line-height:1;display:flex;align-items:center;justify-content:center;gap:10px}
.brand .dot{display:inline-block;border-radius:50%;background:var(--green)}
.tagline{font-family:var(--head);color:var(--ink-soft);text-align:center}
.green-text p,.body-text p{text-align:justify}
.green-text{color:#fff}
.hl{color:var(--yellow);font-weight:600}
.b{font-weight:600}

/* stage boxes */
.stage{position:absolute;left:16px;width:300px;border:2.5px solid;border-radius:6px;background:#fff;text-align:center;padding:22px 10px 6px}
.stage h3{font-family:var(--head);font-weight:600;font-size:15px;letter-spacing:.4px;color:var(--ink);margin-bottom:2px}
.stage p{font-size:11.2px;line-height:14px;color:var(--ink)}
.stage-icon{position:absolute;width:52px;height:52px;border-radius:50%;left:136px;display:flex;align-items:center;justify-content:center}
.stage-arrow{position:absolute;left:140px;width:46px}
.pill{display:block;background:var(--yellow);border-radius:14px;height:24px;line-height:24px;text-align:center;font-weight:600;font-size:13.5px;letter-spacing:.4px;color:#3a3a3a;margin-bottom:11.5px}

/* process */
.step{position:absolute;left:22px;width:300px;height:56px}
.step .box{position:absolute;top:4px;height:48px;border:1.3px solid #777;border-radius:6px;background:#fff;font-size:9.6px;line-height:11.5px;padding:4px 8px;display:flex;align-items:center;text-align:justify}
.step .num{position:absolute;top:6px;width:30px;height:44px;background:#333;color:#fff;font-weight:600;font-size:17px;display:flex;align-items:center;justify-content:center}
.step .icon{position:absolute;top:0;width:56px;height:56px;border-radius:50%;background:var(--green);display:flex;align-items:center;justify-content:center}
.step.l .icon{left:0}.step.l .num{left:44px;border-radius:0 14px 14px 0}.step.l .box{left:70px;right:0}
.step.r .icon{right:0}.step.r .num{right:44px;border-radius:14px 0 0 14px}.step.r .box{right:70px;left:0}
</style>
</head>
<body>
<div class="canvas">

  <!-- ===== OUTSIDE ===== -->
  <div class="spread" style="left:92px;top:1155px;width:1012px;height:730px">

    <!-- left panel: the three stages -->
    <section class="panel" style="left:0;width:332px">
      <div class="branch" role="img" aria-label="Illustration of a brown tree branch with green leaves" style="left:0;top:0;width:332px;height:150px;clip-path:polygon(0 0,100% 0,100% 40%,70% 60%,30% 80%,0 100%)"></div>

      <div class="stage" style="top:188px;height:110px;border-color:var(--blue)">
        <h3>UNDERSTANDING</h3>
        <p>Assessment starts with listening first, and then asking the right questions in order to ensure that we are understanding your concerns and hearing your questions.</p>
      </div>
      <div class="stage-icon" style="top:164px;background:var(--blue)">
        <svg width="28" height="26" viewBox="0 0 28 26" fill="#fff"><circle cx="14" cy="5" r="3"/><circle cx="8" cy="13" r="3.4"/><circle cx="20" cy="13" r="3.4"/><path d="M2 25c0-5 3-7 6-7s6 2 6 7zM14 25c0-5 3-7 6-7s6 2 6 7z"/></svg>
      </div>
      <svg class="stage-arrow" style="top:297px" height="52" viewBox="0 0 46 52"><path d="M0 0h46v36L23 52 0 36z" fill="var(--blue)"/></svg>

      <div class="stage" style="top:380px;height:110px;border-color:var(--teal)">
        <h3>IDENTIFYING</h3>
        <p>It is then our job to use our diagnostic &amp; assessment knowledge and skills to collect the right data in order to address your concerns and provide answers to your questions.</p>
      </div>
      <div class="stage-icon" style="top:356px;background:var(--teal)">
        <svg width="28" height="28" viewBox="0 0 28 28" fill="none" stroke="#fff" stroke-width="3"><circle cx="12" cy="12" r="8"/><path d="M18 18l7 7"/></svg>
      </div>
      <svg class="stage-arrow" style="top:489px" height="52" viewBox="0 0 46 52"><path d="M0 0h46v36L23 52 0 36z" fill="var(--teal)"/></svg>

      <div class="stage" style="top:575px;height:110px;border-color:var(--green)">
        <h3>GUIDING</h3>
        <p>This then enables us to provide you with recom­mendations for accessing support and interven­tions that are based on current best practice &amp; are suported by evidence.</p>
      </div>
      <div class="stage-icon" style="top:551px;background:var(--leaf)">
        <svg width="28" height="26" viewBox="0 0 28 26" fill="none" stroke="#fff" stroke-width="2.4"><path d="M2 8l12-6 12 6v16H2z"/><path d="M9 24v-9h10v9"/></svg>
      </div>
    </section>

    <!-- middle panel: about us -->
    <section class="panel" style="left:332px;width:332px;background:var(--green)">
      <div class="abs" style="left:0;top:-140px;width:332px;height:280px;border-radius:0 0 166px 166px;background:#fff"></div>
      <div class="abs" style="left:0;top:38px;width:332px">
        <div class="brand" style="font-size:40px"><span class="dot" style="width:14px;height:14px"></span>rootwell</div>
        <div class="tagline" style="font-size:11px;margin-top:8px">diagnostic and educational assessments</div>
      </div>
      <h2 class="abs" style="left:0;width:332px;top:168px;text-align:center;font-family:var(--head);font-weight:600;font-size:34px;color:#fff;letter-spacing:.5px">ABOUT US</h2>
      <div class="abs green-text" style="left:20px;width:292px;top:212px;font-size:12.3px;line-height:13.2px">
        <p><span class="hl">rootwell</span> is a team with a passion for help­ing people to thrive. We believe that all people are unique and have different sets of strengths and weaknesses. Some people have particular challenges that impact on their ability to learn, communicate, or engage effectively within communities.</p>
        <p style="margin-top:13px">We believe that children who are finding school­ing challenging need us to understand their challenges and meet them where they need us. While we are passionate about education, we recognise that some people find school and formal learning to be an exercise in survival rather than a place of flourishing. We love to help people to understand their struggles &amp; strengths, this then allowing us to provide guidance for support that is evidence-based and appropriate.</p>
        <p style="margin-top:13px">To that end, we do not provide intervention or treatment ourselves. We are experts focused on assessment and diagnostics who can then help you to access appropriate help, working effective­ly with your school or workplace, applying for fi­nancial support if available (such as NDIS funding), and feel more confident in your decisions.</p>
      </div>
      <div class="abs" style="left:0;top:580px;width:332px;height:150px;background:var(--yellow);text-align:center;padding-top:18px">
        <div style="font-family:var(--head);font-weight:600;font-size:23px;color:var(--ink)">rootwell</div>
        <svg width="120" height="20" viewBox="0 0 120 20" style="margin-top:4px" fill="var(--ink)">
          <path d="M10 1a6 6 0 0 0-6 6c0 5 6 12 6 12s6-7 6-12a6 6 0 0 0-6-6zm0 8.5a2.5 2.5 0 1 1 0-5 2.5 2.5 0 0 1 0 5z"/>
          <path d="M33 4h18v12H33z"/><path d="M33 4l9 7 9-7" fill="none" stroke="var(--yellow)" stroke-width="1.6"/>
          <circle cx="76" cy="10" r="8"/><path d="M68 10h16M76 2c-3 4-3 12 0 16M76 2c3 4 3 12 0 16" stroke="var(--yellow)" stroke-width="1.2" fill="none"/>
          <path d="M102 3c2 0 3 4 2 5l-2 1c1 3 3 5 6 6l1-2c1-1 5 0 5 2l-1 3c-7 1-15-7-14-14z"/>
        </svg>
        <div style="font-size:11.2px;line-height:14.5px;margin-top:4px;color:var(--ink)">7/21 Wattle Ridge Rd, Kelso Bay NSW 2199<br>info@rootwellclinic.com.au<br>www.rootwellclinic.com.au<br>02 5550 1482</div>
      </div>
    </section>

    <!-- right panel: cover -->
    <section class="panel" style="left:664px;width:348px">
      <div class="leaf-pattern" role="img" aria-label="Faint repeating pattern of small leaf figures" style="left:0;top:0;width:348px;height:420px"></div>
      <div class="branch" role="img" aria-label="Illustration of a brown tree branch with green leaves" style="left:0;top:0;width:348px;height:140px;clip-path:polygon(0 0,100% 0,100% 100%,60% 45%,0 30%)"></div>
      <div class="abs" style="left:0;width:348px;top:300px;text-align:center;font-family:var(--head);font-weight:700;font-size:32px;line-height:38px;letter-spacing:1px">
        <div style="color:var(--ink)">UNDERSTANDING</div>
        <div style="color:var(--leaf)">IDENTIFYING</div>
        <div style="color:var(--ink)">GUIDING</div>
      </div>
      <div class="abs" style="left:0;width:348px;top:470px">
        <div class="brand" style="font-size:52px"><span class="dot" style="width:18px;height:18px"></span>rootwell</div>
        <div class="tagline" style="font-size:14px;margin-top:12px">diagnostic and educational assessments</div>
      </div>
      <div class="abs" style="left:37px;top:680px;width:276px;height:34px;border-radius:17px;background:var(--green);color:#fff;font-family:var(--head);font-weight:600;font-size:19px;line-height:34px;text-align:center">www.rootwellclinic.com.au</div>
    </section>
  </div>
  <div class="spread-label" style="left:92px;top:1098px">BROCHURE OUTSIDE</div>

  <!-- ===== INSIDE ===== -->
  <div class="spread" style="left:88px;top:1937px;width:1012px;height:713px">

    <!-- left panel: who we are -->
    <section class="panel" style="left:0;width:336px">
      <div class="abs" role="img" aria-label="Photo of a mother helping her young son with homework at a table" style="left:0;top:0;width:336px;height:278px;background:linear-gradient(135deg,#f3ece4 0%,#e6d8c8 50%,#dfe6ee 100%);border-bottom-right-radius:260px 220px;border-right:6px solid var(--green);border-bottom:6px solid var(--green)"></div>
      <h2 class="abs" style="left:0;width:336px;top:296px;text-align:center;font-family:var(--head);font-weight:600;font-size:26px;letter-spacing:.5px">WHO WE ARE</h2>
      <div class="abs body-text" style="left:27px;width:288px;top:335px;font-size:13.6px;line-height:16.2px;color:var(--ink)">
        <p><span class="b">rootwell</span> is a team with a passion for helping people to thrive. We are a team of psychologists and teachers who have experience in both educational and clinical settings.</p>
        <p style="margin-top:16px">We understand the challenges parents face in wanting what is best for their children, trying to understand how and where to access the most relevant information and support.</p>
      </div>
      <div class="abs" role="img" aria-label="Illustration of a head silhouette with a glowing brain" style="left:0;top:530px;width:336px;height:200px;background:linear-gradient(160deg,#2a2540 0%,#6a3a3a 50%,#f2a24a 100%);border-top-right-radius:320px 180px;border-top:5px solid var(--green);border-right:5px solid var(--green)"></div>
    </section>

    <!-- middle panel: diagnoses -->
    <section class="panel" style="left:336px;width:336px;background:var(--green)">
      <div class="abs green-text" style="left:24px;width:290px;top:42px;font-size:12.6px;line-height:16.2px">
        <p>We are passionate about wanting to help families navigate the diagnostic &amp; assessment process.</p>
        <p style="margin-top:16px">We believe that quality and comprehensive assessment needs to happen before interven­tion begins. We work collaboratively with other professionals to ensure that recommendations and supports put in place are appropriate and evidence-based while also meeting the needs of the individual.</p>
        <p style="margin-top:16px">We are qualified to give formal diagnoses for mental health conditions and specific learning disorders. This includes:</p>
      </div>
      <div class="abs" style="left:20px;width:300px;top:305px">
        <span class="pill">Attention Deficit Hyperactivity Disorder.</span>
        <span class="pill">Autism Spectrum Disorder.</span>
        <span class="pill">Specific Learning Disorders.</span>
        <span class="pill">Language disorders.</span>
        <span class="pill">Anxiety Disorders.</span>
        <span class="pill">Mood Disorders.</span>
        <span class="pill">Communication Disorders.</span>
      </div>
      <div class="abs green-text" style="left:24px;width:290px;top:566px;font-size:12.6px;line-height:16.2px">
        <p>We are passionate about collaborating with your school or workplace, supporting you in applying for financial support if available (such as NDIS funding), and to feel more informed and confident in your decisions.</p>
      </div>
      <div class="abs" style="left:0;width:336px;top:670px;text-align:center;font-family:var(--head);font-weight:600;font-size:20px;color:#fff">www.rootwellclinic.com.au</div>
    </section>

    <!-- right panel: the process -->
    <section class="panel" style="left:672px;width:340px">
      <div class="branch" role="img" aria-label="Illustration of a brown tree branch with green leaves" style="left:0;top:0;width:340px;height:80px;clip-path:polygon(5% 0,100% 0,100% 55%,70% 100%,30% 60%)"></div>
      <h2 class="abs" style="left:0;width:340px;top:112px;text-align:center;font-family:var(--head);font-weight:600;font-size:26px;letter-spacing:.5px">THE PROCESS</h2>
      <svg class="abs" style="left:0;top:150px" width="340" height="340" viewBox="0 0 340 340" fill="none" stroke="#777" stroke-width="1.3">
        <path d="M322 30h12v60h-12M18 88H8v72h14M322 165h12v70h-12M18 235H8v72h14"/>
      </svg>
      <div class="step l" style="top:152px"><div class="icon"><svg width="30" height="28" viewBox="0 0 30 28" fill="#fff"><circle cx="15" cy="6" r="4"/><path d="M7 20c0-5 4-8 8-8s8 3 8 8z"/><rect x="3" y="21" width="24" height="4"/></svg></div><div class="num">01</div><div class="box">An initial face-to-face interview to discuss your concerns and understand the relevant history &amp; details.</div></div>
      <div class="step r" style="top:228px"><div class="icon"><svg width="26" height="30" viewBox="0 0 26 30" fill="none" stroke="#fff" stroke-width="2.4"><rect x="3" y="4" width="20" height="24" rx="2"/><path d="M8 14l4 4 7-8"/></svg></div><div class="num">02</div><div class="box">A formal assessment sessions during which relevant tests are completed. This can in­clude IQ testing, Achievement testing, Memory testing, Personality profiling etc.</div></div>
      <div class="step l" style="top:306px"><div class="icon"><svg width="30" height="28" viewBox="0 0 30 28" fill="#fff"><circle cx="15" cy="6" r="4"/><path d="M7 20c0-5 4-8 8-8s8 3 8 8z"/><rect x="3" y="21" width="24" height="4"/></svg></div><div class="num">03</div><div class="box">Obtaining additional information through questionnaires, observation, contact with other professionals (such as teachers/ tutors etc).</div></div>
      <div class="step r" style="top:384px"><div class="icon"><svg width="26" height="30" viewBox="0 0 26 30" fill="none" stroke="#fff" stroke-width="2.4"><rect x="3" y="4" width="20" height="24" rx="2"/><path d="M8 14l4 4 7-8"/></svg></div><div class="num">04</div><div class="box">A feedback session during which we pro­vide you with a final draft of the report and discuss possible recommendations, collaborating about the next steps.</div></div>
      <div class="step l" style="top:460px"><div class="icon"><svg width="30" height="28" viewBox="0 0 30 28" fill="#fff"><circle cx="15" cy="6" r="4"/><path d="M7 20c0-5 4-8 8-8s8 3 8 8z"/><rect x="3" y="21" width="24" height="4"/></svg></div><div class="num">05</div><div class="box">An initial face-to-face interview to discuss your concerns and understand the relevant history &amp; details.</div></div>
      <div class="abs" style="left:0;width:340px;top:590px">
        <div class="brand" style="font-size:48px"><span class="dot" style="width:16px;height:16px"></span>rootwell</div>
        <div class="tagline" style="font-size:13.5px;margin-top:12px">diagnostic and educational assessments</div>
      </div>
    </section>
  </div>
  <div class="spread-label" style="left:103px;top:2676px">BROCHURE INSIDE</div>

</div>
</body>
</html>
```